Real Estate Investor needs awesome business card design

I invest in real estate, focused on multi-family properties, and I need a business card to hand out to potential partners. I prefer simple, clean designs, but it needs to stand out, so I'd like there to be a bit of red in the design as well.

It should include this information:

Front
Dallin Pecksworth
Real Estate Investor
Direct phone: 502-867-3394
Email: dallinhpecksworth@quillmail.example
Headshot (Picture), I've uploaded a few, just pick the one you think looks best with your design. You can remove the background from the headshot image if it looks better.

Back
The back of the card's design should flow and be congruent with the front. On the back I want to put an inspirational quote or question. There will be different ones depending on the card, so I'll need the original file so I can edit it in the end.

For now, use “The Pessimist Sees Difficulty In Every Opportunity. The Optimist Sees The Opportunity In Every Difficulty.” -Barnaby Ellsworth

Target Market(s)

Investors

Industry/Entity Type

Real Estate

Contact Information for Business Card

Front
Dallin Pecksworth
Real Estate Investor

Back
The back of the card's design should flow and be congruent with the front. On the back I want to put an inspirational quote or question. There will be different ones depending on the card, so I'll need the original file so I can edit it in the end. I've uploaded some EXAMPLES of business cards with quotes on them. Don't copy but feel free to use them as inspiration.

The design will be printed on "ZIB sized" business cards
1039 x 697 pixels
with rounded corners

Font styles to use
Serif
Decorative
Script

Colors
ec1f27

Requirements
Must have
• Headshot, name, and other information in it.
• 1039 x 697 pixels
• Rounded corners
• Clean design that pops. I'm open to see any color background, including black.
• Headshots can be located here: https://www.filecrate.example/sh/8kd2wq7mzt31hvx/BBQTXP4ruf9LmQ0KhcvWx7b?dl=0
Nice to have
• It would be awesome if the design included a personal signature or monogram, but if not I'll get a personal logo developed later and the card redesigned if I think it needs it.
Should not have
• Cluttered design

```html
<!DOCTYPE html>
<html lang="en">
<head>
<meta charset="utf-8">
<title>Dallin Pecksworth — Business Card</title>
<link rel="stylesheet" href="https://fonts.googleapis.com/css2?family=Roboto+Slab:wght@300;400;700&display=swap">
<style>
  :root {
    --card-red: #ec1f27;
    --accent-yellow: #fff200;
    --ink-white: #ffffff;
    --backdrop: #4a3a3c;
    --suit-navy: #1f2740;
    --skin-tone: #e2ab92;
  }
  * { margin: 0; padding: 0; box-sizing: border-box; }
  html, body {
    width: 1200px; height: 1200px; overflow: hidden;
    background: var(--backdrop);
    font-family: "Roboto Slab", Georgia, serif;
  }
  .canvas { position: relative; width: 1200px; height: 1200px; }
  .card {
    position: absolute;
    left: 291px;
    width: 618px; height: 354px;
    background: var(--card-red);
    border-radius: 16px;
    overflow: hidden;
  }
  .card--front { top: 206px; }
  .card--back { top: 642px; }

  .quote-mark { position: absolute; fill: var(--accent-yellow); }
  .card--front .quote-mark--open { left: 44px; top: 45px; width: 76px; height: 70px; }
  .card--back .quote-mark--open { left: 38px; top: 40px; width: 76px; height: 70px; }
  .card--back .quote-mark--close { left: 510px; top: 249px; width: 76px; height: 70px; }

  .identity { position: absolute; left: 44px; top: 140px; color: var(--ink-white); z-index: 2; }
  .identity__name { font-size: 24px; font-weight: 700; line-height: 30px; white-space: nowrap; }
  .identity__role { font-size: 16px; font-weight: 300; color: var(--accent-yellow); line-height: 20px; }
  .contact { margin-top: 16px; font-size: 14px; font-weight: 300; line-height: 21px; white-space: nowrap; }
  .contact__label { color: var(--accent-yellow); display: inline-block; width: 50px; }

  .headshot {
    position: absolute; left: 250px; top: 21px; width: 368px; height: 333px;
  }
  .headshot__head {
    position: absolute; left: 162px; top: 0; width: 160px; height: 270px;
    border-radius: 48% 48% 45% 45%;
    background: linear-gradient(180deg, #b89478 0%, var(--skin-tone) 25%, #d49c80 100%);
  }
  .headshot__body {
    position: absolute; left: 0; top: 232px; width: 368px; height: 122px;
    clip-path: polygon(4% 100%, 30% 40%, 52% 10%, 76% 0, 88% 25%, 100% 100%);
    background: linear-gradient(180deg, #2b3352, var(--suit-navy));
  }

  .quote {
    position: absolute; left: 0; right: 0; top: 114px;
    text-align: center; color: var(--ink-white);
    font-size: 24px; font-weight: 700; line-height: 29.5px;
  }
  .quote__highlight { color: var(--accent-yellow); }
  .quote__author {
    position: absolute; left: 0; right: 0; top: 260px;
    text-align: center; color: var(--accent-yellow);
    font-size: 16px; font-weight: 300;
  }
</style>
</head>
<body>
<div class="canvas">
  <section class="card card--front">
    <svg class="quote-mark quote-mark--open" viewBox="0 0 76 70" aria-hidden="true">
      <path d="M0 70V38C0 18 10 5 28 0l3 10c-9 5-12 12-12 20h12v40Z"/>
      <path d="M45 70V38C45 18 55 5 73 0l3 10c-9 5-12 12-12 20h12v40Z"/>
    </svg>
    <div class="headshot" role="img" aria-label="Headshot of Dallin Pecksworth, smiling, in a navy suit and white shirt, background removed">
      <div class="headshot__body"></div>
      <div class="headshot__head"></div>
    </div>
    <div class="identity">
      <h1 class="identity__name">Dallin Pecksworth</h1>
      <p class="identity__role">Real Estate Investor</p>
      <p class="contact"><span class="contact__label">phone</span>: 502-867-3394<br>
      <span class="contact__label">Email</span>: dallinhpecksworth@quillmail.example</p>
    </div>
  </section>

  <section class="card card--back">
    <svg class="quote-mark quote-mark--open" viewBox="0 0 76 70" aria-hidden="true">
      <path d="M0 70V38C0 18 10 5 28 0l3 10c-9 5-12 12-12 20h12v40Z"/>
      <path d="M45 70V38C45 18 55 5 73 0l3 10c-9 5-12 12-12 20h12v40Z"/>
    </svg>
    <blockquote class="quote">
      The <span class="quote__highlight">Pessimist</span> Sees<br>
      Difficulty In Every Opportunity.<br>
      The <span class="quote__highlight">Optimist</span> Sees<br>
      The Opportunity In Every Difficulty.
    </blockquote>
    <p class="quote__author">{ Barnaby Ellsworth }</p>
    <svg class="quote-mark quote-mark--close" viewBox="0 0 76 70" aria-hidden="true">
      <path d="M31 0v32c0 20-10 33-28 38L0 60c9-5 12-12 12-20H0V0Z"/>
      <path d="M76 0v32c0 20-10 33-28 38l-3-10c9-5 12-12 12-20H45V0Z"/>
    </svg>
  </section>
</div>
</body>
</html>
```